QMWN timeline design

We need a facebook design for our established business which is Australia wide however based in Melbourne. We are a young team of Financial Planners who specialize in Insurance and Basic super advice for people like us.

We are people who help our clients get things done in a timely and cost effective manner whilst having a good time and a laugh along the way.

We do not want it to feel like the standard financial facebook page at all! We would like this to have a consistent feel with our new e-brochure which i have attached from a color and font perspective.

We would also like it to be very easy for people to be able to tell what we do from looking at the page
Updates

Reason: Would like time to respond to preferred designs and have re-works done before comitting

Target Market(s)

We work best with client from 25-40 who are time poor singles, young families and self-made entrepreneurs

Industry/Entity Type

Financial

```html
<!DOCTYPE html>
<html lang="en">
<head>
<meta charset="utf-8">
<title>QMWN timeline cover</title>
<link rel="stylesheet" href="https://fonts.googleapis.com/css2?family=Roboto:wght@400;500;700&display=swap">
<style>
:root{
  --green:#6cbd45;
  --green-deep:#00a651;
  --green-dark:#1f7a3a;
  --ink:#1d1c1c;
  --charcoal-light:#4b4949;
  --charcoal-dark:#1b1a1a;
  --white:#ffffff;
  --page:#ffffff;
  --btn-bg:#f6f7f9;
  --btn-border:#c5c8cd;
  --btn-text:#333333;
}
*{margin:0;padding:0;box-sizing:border-box}
html,body{width:1200px;height:564px;overflow:hidden;background:var(--page)}
body{font-family:"Roboto",Arial,sans-serif}
.canvas{position:relative;width:1200px;height:564px;background:var(--page)}
.cover{
  position:absolute;left:0;top:0;width:1200px;height:441px;
  background:radial-gradient(ellipse 520px 300px at 640px 170px,var(--charcoal-light) 0%,#2e2d2d 55%,var(--charcoal-dark) 100%);
}
.advice-title{
  position:absolute;left:25px;top:60px;
  color:var(--green);font-weight:400;font-size:39px;line-height:40px;letter-spacing:.5px;
}
.process{position:absolute;left:395px;top:66px}
.step-label{
  position:absolute;top:183px;color:var(--white);font-weight:700;font-size:22px;
  transform:translateX(-50%);white-space:nowrap;letter-spacing:.2px;
}
.tagline{
  position:absolute;left:282px;top:338px;
  color:var(--green);font-size:37px;line-height:43px;font-weight:400;
}
.contacts{position:absolute;left:843px;top:288px;list-style:none}
.contact{display:flex;align-items:center;height:36px;margin-bottom:17px}
.contact-icon{width:36px;height:36px;flex:none}
.contact-text{margin-left:14px;color:var(--white);font-weight:700;font-size:17px}
.profile{
  position:absolute;left:27px;top:276px;width:239px;height:236px;
  background:var(--white);border:1px solid #cfd2d6;padding:6px;
}
.profile-inner{
  width:100%;height:100%;background:var(--ink);
  display:flex;align-items:center;justify-content:center;
}
.profile-name{color:var(--green);font-weight:700;font-size:52px;letter-spacing:2px}
.actions{position:absolute;top:467px;left:821px;display:flex;gap:17px}
.btn{
  height:34px;border:1px solid var(--btn-border);background:var(--btn-bg);border-radius:2px;
  color:var(--btn-text);font-weight:700;font-size:17px;display:flex;align-items:center;padding:0 12px;
}
.btn-group{display:flex}
.btn-gear{width:61px;justify-content:center;border-left:none;gap:6px;padding:0}
</style>
</head>
<body>
<main class="canvas">
  <section class="cover">
    <h1 class="advice-title">OUR<br>FINANCIAL<br>ADVICE</h1>

    <svg class="process" width="520" height="120" viewBox="0 0 520 120" aria-label="Discovery, strategy, implementation">
      <defs>
        <radialGradient id="tickFill" cx="50%" cy="40%" r="60%">
          <stop offset="0" stop-color="#14b864"/>
          <stop offset="1" stop-color="#008a43"/>
        </radialGradient>
      </defs>
      <path d="M70 48 Q160 40 256 48 Q350 40 447 48 L447 72 Q350 80 256 72 Q160 80 70 72 Z" fill="var(--green)"/>
      <g>
        <circle cx="70" cy="60" r="53" fill="var(--green)"/>
        <circle cx="70" cy="60" r="42" fill="var(--green-dark)"/>
        <circle cx="70" cy="60" r="39" fill="url(#tickFill)"/>
        <path d="M53 58 L66 72 L90 45" fill="none" stroke="#173d24" stroke-width="6" stroke-linecap="round" stroke-linejoin="round"/>
      </g>
      <g>
        <circle cx="256" cy="60" r="53" fill="var(--green)"/>
        <circle cx="256" cy="60" r="42" fill="var(--green-dark)"/>
        <circle cx="256" cy="60" r="39" fill="url(#tickFill)"/>
        <path d="M239 58 L252 72 L276 45" fill="none" stroke="#173d24" stroke-width="6" stroke-linecap="round" stroke-linejoin="round"/>
      </g>
      <g>
        <circle cx="447" cy="60" r="53" fill="var(--green)"/>
        <circle cx="447" cy="60" r="42" fill="var(--green-dark)"/>
        <circle cx="447" cy="60" r="39" fill="url(#tickFill)"/>
        <path d="M430 58 L443 72 L467 45" fill="none" stroke="#173d24" stroke-width="6" stroke-linecap="round" stroke-linejoin="round"/>
      </g>
    </svg>
    <span class="step-label" style="left:465px">DISCOVERY</span>
    <span class="step-label" style="left:653px">STRATEGY</span>
    <span class="step-label" style="left:843px">IMPLEMENTATION</span>

    <p class="tagline">SECURE FUTURE,<br>ENHANCED LIFESTYLE</p>

    <ul class="contacts">
      <li class="contact">
        <svg class="contact-icon" viewBox="0 0 36 36" aria-hidden="true">
          <rect x="2" y="2" width="32" height="32" fill="var(--white)" stroke="var(--green)" stroke-width="4"/>
          <path d="M12 9 L15 9 L17 14 L15 16 Q17 21 21 23 L23 21 L28 23 L28 26 Q27 28 24 28 Q13 26 9 13 Q9 10 12 9 Z" fill="var(--ink)"/>
        </svg>
        <span class="contact-text">1300 555 014</span>
      </li>
      <li class="contact">
        <svg class="contact-icon" viewBox="0 0 36 36" aria-hidden="true">
          <rect x="2" y="2" width="32" height="32" fill="var(--white)" stroke="var(--green)" stroke-width="4"/>
          <rect x="9" y="11" width="18" height="14" fill="none" stroke="var(--ink)" stroke-width="2"/>
          <path d="M9 11 L18 19 L27 11" fill="none" stroke="var(--ink)" stroke-width="2"/>
        </svg>
        <span class="contact-text">admin@qmwn.com.au</span>
      </li>
      <li class="contact">
        <svg class="contact-icon" viewBox="0 0 36 36" aria-hidden="true">
          <rect x="2" y="2" width="32" height="32" fill="var(--white)" stroke="var(--green)" stroke-width="4"/>
          <text x="18" y="25" text-anchor="middle" font-family="Roboto, Arial, sans-serif" font-weight="700" font-size="21" fill="var(--ink)">@</text>
        </svg>
        <span class="contact-text">www.qmwnplanning.com.au</span>
      </li>
    </ul>
  </section>

  <div class="profile">
    <div class="profile-inner"><span class="profile-name">QMWN</span></div>
  </div>

  <nav class="actions">
    <span class="btn">Update Info</span>
    <span class="btn-group">
      <span class="btn">Activity Log</span>
      <span class="btn btn-gear">
        <svg width="14" height="14" viewBox="0 0 14 14" aria-hidden="true">
          <circle cx="7" cy="7" r="4.5" fill="none" stroke="#444" stroke-width="2.6" stroke-dasharray="2 1.55"/>
          <circle cx="7" cy="7" r="2.6" fill="#444"/>
        </svg>
        <svg width="10" height="6" viewBox="0 0 10 6" aria-hidden="true"><path d="M0 0 L10 0 L5 6 Z" fill="#5b7bc0"/></svg>
      </span>
    </span>
  </nav>
</main>
</body>
</html>
```